Brightpath Ventures Inc. Business Cards

We provide services for executives in mid-sized ($250M - $1B) and large companies ($1B +) for who manage their indirect channels. Indirect channels are when 3rd parties that sell a companies products. Examples are the managers in companies that supervise agent, dealer, reseller channels including insurance, auto dealers, technology resellers, and other agent and dealer channels. These services (the Seven Keys) include attracting the best channel resellers, advancing their skills, activating inactive resellers, awarding your resellers with compensation and incentives, and advertising your channel with new marketing
Updates

Thank you for your designs - they all look great.  I realize that I forgot to include a few items.  The items below need to be added to my card design:

Lionel Pratt
CEO / Founder
(This is above the address)
(Below the address) (use email & Website icon)
lionel.pratt@brightpathventures.example
website:  www.brightpathventures.example
(Note:  Please use icon from Twitter, Linkedin, and Skype)
(Twitter) #BrightpathVentures
(Skype):  lioneledwardpratt

Target Market(s)

Business Executives responsible for their indirect channel

Industry/Entity Type

Advertising

Contact Information for Business Card

PO Box 419
2381 Hollinwood Lane
Centerville MA 02617 USA
+1 508.555.0193

Colors

Designer to choose colors to be used in the design.

Requirements
Must have
• Front: I'd prefer a simple design - white background. Logo, contact information, and tag line "Shaping Stronger Networks" I have provided two logos 1) The plain logo "Brightpath Ventures" (Front of card) and 2) "The Seven Keys of Brightpath Ventures" (Back of Card).
a) Front: Logo, tag line, contact info, b) Back: Graphic of Seven Keys; plus the following links.
Seven Keys of Brightpath Ventures: http://www.brightpathventures.example/the-seven-keys/
Seven Keys Partner Review:
http://www.brightpathventures.example/keys-partner-review/
Seven Keys Journal:
http://www.brightpathventures.example/category/journal/
Seven Keys Resources:
http://www.brightpathventures.example/get-resources/
Nice to have
• Brightpath Ventures logo on Front and Graphic of the "Seven Keys of Brightpath Ventures" on the back. Match the colors of the logo.

```html
<!DOCTYPE html>
<html lang="en">
<head>
<meta charset="utf-8">
<title>Brightpath Ventures – Card Back</title>
<link href="https://fonts.googleapis.com/css2?family=Bebas+Neue&family=Arimo:wght@700&display=swap" rel="stylesheet">
<style>
  :root {
    --brand-blue: #1638f2;
    --brand-green: #5ee21c;
    --ink-grey: #5e5e5e;
    --paper: #ffffff;
    --mark-fill: #2f6cf0;
  }
  * { box-sizing: border-box; margin: 0; padding: 0; }
  html, body {
    width: 1200px;
    height: 702px;
    overflow: hidden;
    background: var(--paper);
  }
  .card {
    position: relative;
    width: 1200px;
    height: 702px;
    background: var(--paper);
  }
  .wordmark {
    position: absolute;
    top: 88px;
    left: 0;
    width: 100%;
    text-align: center;
    font-family: "Bebas Neue", sans-serif;
    font-weight: 400;
    font-size: 87px;
    line-height: 1;
    letter-spacing: 2px;
    color: var(--brand-blue);
  }
  .brand-mark {
    position: absolute;
    left: 505px;
    top: 198px;
    width: 190px;
    height: 190px;
  }
  .tagline {
    position: absolute;
    top: 403px;
    left: 0;
    width: 100%;
    text-align: center;
    font-family: "Arimo", Arial, sans-serif;
    font-weight: 700;
    font-size: 25px;
    color: var(--ink-grey);
  }
  .links {
    position: absolute;
    top: 506px;
    left: 56px;
    right: 20px;
    display: grid;
    grid-template-columns: 519px auto;
    row-gap: 15px;
    font-family: "Bebas Neue", sans-serif;
    line-height: 1.2;
  }
  .link-title {
    display: block;
    font-size: 29px;
  }
  .link-url {
    display: block;
    font-size: 27px;
    color: var(--ink-grey);
  }
  .links .col-left .link-title { color: var(--brand-green); }
  .links .col-right .link-title { color: var(--brand-blue); }
</style>
</head>
<body>
  <main class="card">
    <h1 class="wordmark">BRIGHTPATHVENTURES</h1>

    <svg class="brand-mark" viewBox="0 0 190 190" aria-hidden="true">
      <circle cx="95" cy="95" r="94" fill="var(--mark-fill)"/>
    </svg>

    <p class="tagline">DISCOVER, DEVELOP, ENGAGE, REWARD, PROMOTE</p>

    <section class="links">
      <div class="link-item col-left">
        <span class="link-title">SEVEN KEYS OF BRIGHTPATH VENTURES</span>
        <span class="link-url">BRIGHTPATHVENTURES.EXAMPLE/THE-SEVEN-KEYS</span>
      </div>
      <div class="link-item col-right">
        <span class="link-title">SEVEN KEYS JOURNAL</span>
        <span class="link-url">BRIGHTPATHVENTURES.EXAMPLE/CATEGORY/JOURNAL</span>
      </div>
      <div class="link-item col-left">
        <span class="link-title">SEVEN KEYS PARTNER REVIEW</span>
        <span class="link-url">BRIGHTPATHVENTURES.EXAMPLE/KEYS-PARTNER-REVIEW</span>
      </div>
      <div class="link-item col-right">
        <span class="link-title">SEVEN KEYS RESOURCES</span>
        <span class="link-url">BRIGHTPATHVENTURES.EXAMPLE/GET-RESOURCES</span>
      </div>
    </section>
  </main>
</body>
</html>
```